RK Bastone Construction Inc.

Design a new business card for our construction company
To be removed from current card:
Delete 25 years
Delete Tenant fit up Renovations section

```html
<!DOCTYPE html>
<html lang="en">
<head>
<meta charset="utf-8">
<title>RK Bastone Construction Inc. — Business Card</title>
<link rel="stylesheet" href="https://fonts.googleapis.com/css2?family=Montserrat:wght@400;500;700;800&display=swap">
<style>
  :root {
    --purple-deep: #4f2b70;
    --purple-mid: #6a3f8c;
    --purple-light: #80589f;
    --teal: #2a8a7c;
    --ink: #2b2b2b;
    --paper: #ffffff;
    --page: #e6e6e8;
    --white: #ffffff;
  }
  * { box-sizing: border-box; margin: 0; padding: 0; }
  html, body {
    width: 1200px; height: 1200px; overflow: hidden;
    background: var(--page);
    font-family: "Montserrat", Arial, sans-serif;
  }
  .canvas { position: relative; width: 1200px; height: 1200px; }

  .card {
    position: absolute; left: 180px; width: 840px; height: 480px;
    box-shadow: 0 10px 30px rgba(0,0,0,0.18);
    overflow: hidden;
  }
  .card--front {
    top: 80px;
    background: radial-gradient(ellipse at 35% 75%, var(--purple-light) 0%, var(--purple-mid) 45%, var(--purple-deep) 100%);
    display: flex; align-items: center; justify-content: center;
  }
  .card--back { top: 640px; background: var(--paper); }

  .wordmark {
    font-weight: 700; letter-spacing: 1px; text-transform: uppercase;
    line-height: 1.1; text-align: center;
  }
  .card--front .wordmark { color: var(--white); font-size: 46px; }

  .services {
    position: absolute; left: 60px; top: 56px; width: 340px;
    text-align: right; color: var(--ink); font-size: 17px; line-height: 1.45;
  }
  .services .sectors { font-weight: 700; margin-top: 4px; }

  .card--back .wordmark {
    position: absolute; right: 44px; top: 150px; width: 360px;
    color: var(--purple-mid); font-size: 28px; text-align: right;
  }

  .holder {
    position: absolute; left: 300px; top: 250px; text-align: left;
  }
  .holder-name { color: var(--teal); font-weight: 800; font-size: 32px; line-height: 1.2; }
  .contact { display: flex; align-items: center; gap: 8px; color: var(--ink); font-size: 18px; line-height: 1.2; }
  .contact svg { width: 16px; height: 16px; flex: none; }
  .holder .contact { margin-top: 8px; margin-left: 6px; }

  .office-phone { position: absolute; left: 40px; top: 340px; }
  .email { position: absolute; right: 40px; top: 340px; }
  .rule { position: absolute; left: 40px; right: 40px; height: 2px; background: var(--purple-mid); }
  .rule--upper { top: 370px; }
  .rule--lower { top: 420px; }
  .website { position: absolute; left: 0; right: 0; top: 383px; justify-content: center; }
  .address { position: absolute; left: 0; right: 0; top: 440px; text-align: center; color: var(--ink); font-size: 17px; line-height: 1.2; }
</style>
</head>
<body>
<main class="canvas">
  <section class="card card--front" aria-label="Card front">
    <p class="wordmark">RK Bastone<br>Construction Inc.</p>
  </section>

  <section class="card card--back" aria-label="Card back">
    <div class="services">
      <p>Turn Key Operations</p>
      <p>Project Management</p>
      <p class="sectors">Office | Retail | Institutional</p>
    </div>

    <p class="wordmark">RK Bastone<br>Construction Inc.</p>

    <div class="holder">
      <p class="holder-name">Dario Bastone</p>
      <p class="contact">
        <svg viewBox="0 0 16 16" aria-hidden="true"><path fill="var(--teal)" d="M3.5 1.5l2.5 0 1 3.5-1.6 1.2a8 8 0 0 0 4.4 4.4L11 9l3.5 1v2.5c0 1-1 2-2 2C6.5 14.5 1.5 9.5 1.5 3.5c0-1 1-2 2-2z"/></svg>
        613-555-0187
      </p>
    </div>

    <p class="contact office-phone">
      <svg viewBox="0 0 16 16" aria-hidden="true"><path fill="var(--teal)" d="M3.5 1.5l2.5 0 1 3.5-1.6 1.2a8 8 0 0 0 4.4 4.4L11 9l3.5 1v2.5c0 1-1 2-2 2C6.5 14.5 1.5 9.5 1.5 3.5c0-1 1-2 2-2z"/></svg>
      613-555-0142 ext. 221
    </p>
    <p class="contact email">
      <svg viewBox="0 0 16 16" aria-hidden="true"><rect x="1" y="3" width="14" height="10" fill="var(--teal)"/><path d="M1 3l7 5 7-5" fill="none" stroke="var(--white)" stroke-width="1.4"/></svg>
      dario@rkbastoneconst.ca
    </p>
    <div class="rule rule--upper"></div>
    <p class="contact website">
      <svg viewBox="0 0 16 16" aria-hidden="true"><circle cx="8" cy="8" r="6.5" fill="none" stroke="var(--teal)" stroke-width="1.5"/><ellipse cx="8" cy="8" rx="3" ry="6.5" fill="none" stroke="var(--teal)" stroke-width="1.2"/><path d="M1.5 8h13" stroke="var(--teal)" stroke-width="1.2"/></svg>
      www.rkbastoneconstruction.ca
    </p>
    <div class="rule rule--lower"></div>
    <p class="address">1280 Millbrook Rd., Suite 100, Ottawa, ON K1B 4T7</p>
  </section>
</main>
</body>
</html>
```